Need a plumbing billboard for our business.

We are a woman owned plumbing company and redoing our billboard and was looking for some fresh ideas... Attached is pic of current billboard..

```html
<!DOCTYPE html>
<html lang="en">
<head>
<meta charset="utf-8">
<title>Lone Range Plumbing Billboard</title>
<link rel="stylesheet" href="https://fonts.googleapis.com/css2?family=Anton&family=Oswald:wght@600&family=Russo+One&display=swap">
<style>
  :root {
    --red: #e11f2e;
    --dark: #262626;
    --white: #ffffff;
    --band: #ececec;
    --ink: #141414;
    --silver: #dcdcdc;
    --seal-rim: #8c8c8c;
    --seal-core: #333333;
    --backdrop: #d9d9d9;
  }
  html, body {
    margin: 0;
    padding: 0;
    width: 996px;
    height: 1200px;
    overflow: hidden;
    background: var(--backdrop);
  }
  .billboard {
    position: absolute;
    left: 28px;
    top: 470px;
    width: 940px;
    height: 260px;
    box-shadow: 0 6px 18px rgba(0,0,0,.25);
  }
  .wordmark, .call, .phone-number, .market { font-family: "Russo One", sans-serif; }
  .services { font-family: "Oswald", sans-serif; font-weight: 600; }
  .ownership { font-family: "Anton", sans-serif; }
  .license { font-family: Arial, Helvetica, sans-serif; }
</style>
</head>
<body>
<svg class="billboard" viewBox="0 0 1520 420" xmlns="http://www.w3.org/2000/svg">
  <defs>
    <linearGradient id="portrait-tone" x1="0" y1="0" x2="0" y2="1">
      <stop offset="0" stop-color="#e8c58f"/>
      <stop offset="0.35" stop-color="#e7b596"/>
      <stop offset="0.55" stop-color="#d61c80"/>
      <stop offset="0.88" stop-color="#c8176f"/>
      <stop offset="1" stop-color="#3a3f5a"/>
    </linearGradient>
  </defs>

  <!-- base panels -->
  <rect class="swoosh" x="0" y="0" width="1520" height="420" fill="var(--red)"/>
  <path class="hero-field" d="M0,0 H1000 C1080,50 1110,140 1100,255 H130 C60,235 15,160 0,70 Z" fill="var(--white)"/>
  <path class="feature-panel" d="M1020,0 H1520 V285 C1420,282 1330,320 1275,420 H1150 C1145,250 1105,100 1020,0 Z" fill="var(--dark)"/>
  <path class="trust-field" d="M1275,420 C1330,326 1420,292 1520,295 V420 Z" fill="var(--white)"/>

  <!-- bands -->
  <rect class="service-band" x="0" y="255" width="1000" height="60" fill="var(--band)"/>
  <rect class="market-band" x="0" y="315" width="1150" height="105" fill="var(--dark)"/>
  <path class="call-band" d="M322,315 H1150 V420 H355 Z" fill="var(--red)"/>

  <!-- portrait area -->
  <rect role="img" aria-label="Photo of the owner, smiling, arms crossed, in a pink blouse" x="1000" y="0" width="270" height="420" fill="url(#portrait-tone)"/>

  <!-- brand -->
  <circle class="brand-dot" cx="205" cy="140" r="62" fill="var(--red)"/>
  <text class="wordmark" x="300" y="165" font-size="104" fill="var(--ink)">Lone Range</text>
  <text class="wordmark" x="520" y="212" font-size="38" letter-spacing="14" fill="var(--ink)">Plumbing</text>

  <!-- services -->
  <g class="services" font-size="36" fill="#222">
    <rect x="42" y="278" width="14" height="14" fill="var(--red)" transform="rotate(45 49 285)"/>
    <text x="74" y="299">PLUMBING</text>
    <rect x="253" y="278" width="14" height="14" fill="var(--red)" transform="rotate(45 260 285)"/>
    <text x="285" y="299">SEPTIC PUMPING</text>
    <rect x="560" y="278" width="14" height="14" fill="var(--red)" transform="rotate(45 567 285)"/>
    <text x="592" y="299">PORTA-POTTY RENTALS</text>
  </g>

  <!-- market -->
  <g class="market" fill="var(--white)">
    <text x="45" y="338" font-size="16">FOR</text>
    <rect x="16" y="356" width="12" height="12" fill="var(--red)" transform="rotate(45 22 362)"/>
    <text x="45" y="374" font-size="33">RESIDENTIAL</text>
    <rect x="16" y="392" width="12" height="12" fill="var(--red)" transform="rotate(45 22 398)"/>
    <text x="45" y="409" font-size="33">COMMERCIAL</text>
  </g>

  <!-- call -->
  <text class="call" x="382" y="350" font-size="32" fill="var(--white)">CALL US TODAY</text>
  <rect class="phone-icon" x="382" y="366" width="40" height="40" rx="9" fill="var(--white)"/>
  <path d="M393,374 c2,-2 5,-2 6,0 l3,5 c1,2 0,4 -2,5 c2,5 5,8 10,10 c1,-2 3,-3 5,-2 l5,3 c2,1 2,4 0,6 l-3,3 c-10,1 -26,-15 -25,-25 Z" fill="var(--red)"/>
  <text class="phone-number" x="438" y="408" font-size="60" letter-spacing="5" fill="var(--white)">555-014-2290</text>

  <!-- ownership -->
  <g class="ownership" font-size="74" fill="var(--silver)" text-anchor="middle">
    <text x="1388" y="82">WOMAN</text>
    <text x="1388" y="150">OWNED</text>
  </g>

  <!-- seals -->
  <g class="seals">
    <g class="seal seal-hours">
      <circle cx="1335" cy="210" r="46" fill="var(--seal-rim)"/>
      <circle cx="1335" cy="210" r="36" fill="var(--seal-core)"/>
      <rect x="1313" y="201" width="44" height="18" rx="3" fill="var(--red)"/>
    </g>
    <g class="seal seal-years">
      <circle cx="1445" cy="210" r="46" fill="var(--seal-rim)"/>
      <circle cx="1445" cy="210" r="36" fill="var(--seal-core)"/>
      <rect x="1419" y="214" width="52" height="16" rx="2" fill="var(--red)"/>
    </g>
  </g>

  <!-- credentials -->
  <g class="credentials">
    <rect x="1240" y="338" width="38" height="48" rx="4" fill="#1f5da8"/>
    <rect x="1294" y="340" width="44" height="44" rx="6" fill="#3b5a9c"/>
    <rect x="1352" y="342" width="92" height="42" rx="6" fill="none" stroke="#2f7d6a" stroke-width="3"/>
    <circle cx="1474" cy="360" r="20" fill="none" stroke="#555" stroke-width="3"/>
  </g>
  <text class="license" x="1485" y="410" font-size="12" fill="#333" text-anchor="end">LICENSE #M-10375</text>
</svg>
</body>
</html>
```